Business Card Design

I need a business card design. I am a sole practitioner.I am a psychotherapist and I need a professional card. I am also an art therapist (a form of psychotherapy using art) so I want the image to be professional/creative/maybe ethnic. I do not want a boring minimalist "medical" image, nor do I want it too hippy/tree hugging.
Colours like reds/ochres/yellows would be good.
Contact Information for Business Card
Mira Hask
Psychotherapy, Counselling and Art Therapy
Wunnara Lodge Counselling and Wellbeing services
17 Pellow Road, Marlow Vale 4190
0417639052 www.MiraHask.com.au
on rear of card I need the option to have at least 4 or 5 appointment times /dates

```html
<!DOCTYPE html>
<html lang="en">
<head>
<meta charset="utf-8">
<title>Mira Hask – Business Card</title>
<link rel="stylesheet" href="https://fonts.googleapis.com/css2?family=Comfortaa:wght@400;500&family=Cormorant+Garamond:wght@500&display=swap">
<style>
  :root {
    --page-bg: #ece8e1;
    --card-light: #f0cf8c;
    --card-mid: #e4b96c;
    --card-deep: #d6a456;
    --ink: #2b1d10;
    --ink-soft: #4a3420;
    --mark: #3a2412;
    --motif: rgba(176, 128, 60, 0.28);
  }
  * { box-sizing: border-box; margin: 0; padding: 0; }
  html, body {
    width: 1200px; height: 784px; overflow: hidden;
    background: var(--page-bg);
  }
  .sheet { position: relative; width: 1200px; height: 784px; }

  .card {
    position: absolute;
    width: 540px; height: 330px;
    background: linear-gradient(160deg, var(--card-light) 0%, var(--card-mid) 60%, var(--card-deep) 100%);
    box-shadow: 0 6px 18px rgba(60, 40, 20, 0.18);
    color: var(--ink);
    font-family: "Comfortaa", sans-serif;
    overflow: hidden;
  }
  .card--back { left: 40px; top: 227px; }
  .card--front { left: 620px; top: 227px; }

  .card-motif {
    position: absolute; inset: 0;
    background:
      radial-gradient(ellipse 90px 70px at 30% 78%, var(--motif), transparent 70%),
      radial-gradient(ellipse 110px 80px at 72% 55%, var(--motif), transparent 70%),
      radial-gradient(ellipse 80px 60px at 88% 20%, var(--motif), transparent 70%),
      linear-gradient(100deg, transparent 40%, rgba(176,128,60,0.12) 50%, transparent 60%);
  }

  .card-frame {
    position: absolute; inset: 10px;
    border: 2px solid var(--ink);
    box-shadow: inset 0 0 0 3px transparent, inset 0 0 0 4px rgba(43,29,16,0.6);
  }

  .brand { position: absolute; display: flex; align-items: flex-start; gap: 14px; }
  .brand-square { background: var(--mark); flex: none; }
  .brand-name { font-weight: 400; color: var(--ink); line-height: 1; letter-spacing: 1px; }
  .brand-tagline {
    font-family: "Cormorant Garamond", serif; font-weight: 500;
    color: var(--ink-soft); white-space: nowrap;
  }

  /* Front */
  .card--front .brand { left: 44px; top: 46px; }
  .card--front .brand-square { width: 100px; height: 100px; }
  .card--front .brand-name { font-size: 50px; margin-top: 4px; }
  .card--front .brand-tagline { font-size: 15px; margin-top: 10px; }

  .contact {
    position: absolute; left: 40px; top: 190px;
    font-size: 15px; line-height: 1.45; color: var(--ink);
    font-style: normal;
  }
  .contact-phone { font-size: 17px; font-weight: 500; }
  .contact-web { font-size: 16px; }

  /* Back */
  .appointment-title {
    position: absolute; left: 32px; top: 28px;
    font-size: 16px; font-weight: 400;
    text-decoration: underline; text-underline-offset: 3px;
  }
  .appointment-rows {
    position: absolute; left: 40px; top: 66px;
    display: grid; grid-template-columns: auto auto; column-gap: 22px; row-gap: 12px;
    font-size: 14px;
  }
  .slot { display: flex; align-items: flex-end; gap: 6px; }
  .slot-line { display: inline-block; border-bottom: 1px dotted var(--ink); height: 14px; }
  .slot--time .slot-line { width: 140px; }
  .slot--date .slot-line { width: 130px; }

  .card--back .brand { left: 290px; top: 232px; gap: 10px; }
  .card--back .brand-square { width: 50px; height: 50px; }
  .card--back .brand-name { font-size: 28px; }
  .card--back .brand-tagline { font-size: 10px; margin-top: 6px; }
</style>
</head>
<body>
<main class="sheet">

  <section class="card card--back" aria-label="Card reverse: appointment times">
    <div class="card-motif" role="img" aria-label="Faint carved tree-trunk and spiral motif"></div>
    <h2 class="appointment-title">Appointment</h2>
    <div class="appointment-rows">
      <div class="slot slot--time">Time: <span class="slot-line"></span></div>
      <div class="slot slot--date">Date: <span class="slot-line"></span></div>
      <div class="slot slot--time">Time: <span class="slot-line"></span></div>
      <div class="slot slot--date">Date: <span class="slot-line"></span></div>
      <div class="slot slot--time">Time: <span class="slot-line"></span></div>
      <div class="slot slot--date">Date: <span class="slot-line"></span></div>
      <div class="slot slot--time">Time: <span class="slot-line"></span></div>
      <div class="slot slot--date">Date: <span class="slot-line"></span></div>
      <div class="slot slot--time">Time: <span class="slot-line"></span></div>
      <div class="slot slot--date">Date: <span class="slot-line"></span></div>
    </div>
    <div class="brand">
      <span class="brand-square"></span>
      <div>
        <div class="brand-name">Mira Hask</div>
        <div class="brand-tagline">Psychotherapy, Counselling and Art Therapy</div>
      </div>
    </div>
  </section>

  <section class="card card--front" aria-label="Card front: contact details">
    <div class="card-motif" role="img" aria-label="Faint carved tree-trunk and spiral motif"></div>
    <div class="card-frame"></div>
    <div class="brand">
      <span class="brand-square"></span>
      <div>
        <h1 class="brand-name">Mira Hask</h1>
        <p class="brand-tagline">Psychotherapy, Counselling and Art Therapy</p>
      </div>
    </div>
    <address class="contact">
      <div>Wunnara Lodge Counselling and Wellbeing services</div>
      <div>17 Pellow Road, Marlow Vale 4190</div>
      <div class="contact-phone">0417639052</div>
      <div class="contact-web">www.MiraHask.com.au</div>
    </address>
  </section>

</main>
</body>
</html>
```